Architectural, Engineering and Design Build

Tavonex4.com
Veteran Disabled Certified company is doing business in Architecture, Engineer and Design build - look simialr websites and come up with design follow following website
https://dorsey-kalbin.example/
https://www.velmonteam.example/
https://www.pirnoqa.example/contract-vehicles/service-disabled-veteran-owned-small-business-sdvosb/
https://www.corbelhubnet.example/about/sdvosb/

Target Market(s)

US - Defense and Federal Government

Industry/Entity Type

Colors
0054AA
0677BA
7BADD7
CADEEF
E8F1F8

Requirements
Must have
• Army, American patriotism , Buildings, construction, architecture, engineering
Nice to have
• I need to attract federal government agencies and Defense

```html
<!DOCTYPE html>
<html lang="en">
<head>
<meta charset="utf-8">
<title>Tavonex4.com — Architecture for Federal Government Agencies and Defense</title>
<link href="https://fonts.googleapis.com/css2?family=Plus+Jakarta+Sans:wght@500;600;700&family=Inter:wght@400;500;600;700&display=swap" rel="stylesheet">
<style>
:root{
  --blue:#0054AA;
  --blue-2:#0677BA;
  --blue-3:#7BADD7;
  --blue-4:#CADEEF;
  --blue-5:#E8F1F8;
  --navy:#0B2748;
  --ink:#1B2434;
  --text:#5A6270;
  --white:#ffffff;
  --line:#D6DEE8;
  --star:#F5A623;
}
*{box-sizing:border-box;margin:0;padding:0}
html,body{width:1200px;height:4608px;overflow:hidden}
body{position:relative;background:var(--white);font-family:"Inter",sans-serif;color:var(--text)}
.abs{position:absolute}
h1,h2,h3,.heading{font-family:"Plus Jakarta Sans",sans-serif;color:var(--ink);font-weight:600}
.eyebrow{font:700 11px/1 "Inter",sans-serif;letter-spacing:1.6px;color:var(--blue);text-transform:uppercase;display:flex;align-items:center;gap:8px}
.eyebrow::before{content:"";width:32px;height:2px;background:currentColor}
.btn{display:flex;align-items:center;justify-content:center;gap:8px;background:var(--blue);color:#fff;font:700 12px/1 "Inter",sans-serif;letter-spacing:1.4px;text-transform:uppercase}
.photo{position:absolute}

/* header */
.topbar{left:760px;top:0;width:440px;height:45px;background:var(--navy);clip-path:polygon(40px 0,100% 0,100% 100%,0 100%)}
.topbar-item{top:14px;color:#fff;font-size:13px;display:flex;align-items:center;gap:7px}
.brand{display:flex;align-items:center;gap:12px;font:700 30px/1 "Plus Jakarta Sans",sans-serif;color:var(--navy)}
.brand-mark{width:52px;height:52px;background:var(--blue);border-radius:6px}
.nav{top:78px;display:flex;font-size:14px;font-weight:500;color:var(--ink)}
.nav a{position:absolute;white-space:nowrap;text-decoration:none;color:inherit}
.nav .active{color:var(--blue)}
.header-rule{left:0;top:125px;width:1200px;height:1px;background:var(--line)}

/* hero */
.hero-title{left:0;top:325px;width:1200px;text-align:center;color:#fff;font:600 38px/52px "Plus Jakarta Sans",sans-serif;text-transform:uppercase}
.hero-btn{left:508px;top:492px;width:184px;height:46px;border:2px solid #fff;background:rgba(0,0,0,.35);color:#fff;font:700 12px/1 "Inter",sans-serif;letter-spacing:1.4px;display:flex;align-items:center;justify-content:center;gap:6px}

.section-title{font-size:34px;line-height:44px}
.para{font-size:14px;line-height:25px}

/* projects */
.proj-card{width:320px;height:448px;background:#fff;box-shadow:0 6px 20px rgba(11,39,72,.08)}
.proj-card .img{height:240px}
.proj-card h3{margin:22px 18px 0;font:600 14px/22px "Inter",sans-serif;color:var(--ink)}
.proj-card p{margin:10px 18px 0;font-size:14px;line-height:24px}
.proj-card .btn{margin:18px 18px 0;width:167px;height:50px}

/* services */
.svc-card{width:324px;height:379px;background:#fff;box-shadow:0 8px 24px rgba(11,39,72,.1);text-align:center}
.svc-card .icon{margin:52px auto 0;width:70px;height:70px;position:relative}
.svc-card h3{margin-top:32px;font:600 17px/1 "Inter",sans-serif;color:var(--ink)}
.svc-card p{margin:20px 30px 0;font-size:14px;line-height:25px}
.svc-card .btn{margin:30px auto 0;width:167px;height:50px}

.logo-strip{left:84px;top:3286px;width:1030px;height:134px;border:1px solid var(--line);display:grid;grid-template-columns:repeat(4,1fr);background:#fff}
.logo-cell{border-right:1px solid var(--line);display:flex;align-items:center;justify-content:center;gap:12px}
.logo-cell:last-child{border-right:none}
.logo-shape{width:52px;height:52px;background:var(--blue-4);border-radius:50%}
.logo-bar{width:90px;height:16px;background:var(--blue-5);border-radius:3px}

/* testimonials */
.review{width:332px;height:326px;background:#fff;box-shadow:0 6px 22px rgba(11,39,72,.08);text-align:center}
.avatar{width:42px;height:42px;border-radius:50%;background:var(--blue);color:#fff;font:600 16px/42px "Inter",sans-serif;margin:22px auto 0}
.review h3{margin-top:12px;font:600 16px/1 "Inter",sans-serif;color:var(--ink)}
.review .role{margin-top:8px;font-size:12px}
.review .stars{margin-top:8px;color:var(--star);font-size:14px;letter-spacing:2px}
.review p{margin:14px 30px 0;font-size:14px;line-height:23px}
.review .src{width:20px;height:20px;border-radius:50%;background:var(--blue-4);margin:20px auto 0}

/* footer */
.footer{left:0;top:4160px;width:1200px;height:448px;background:var(--navy);color:#C9D3E0}
.footer h4{font:600 14px/1 "Inter",sans-serif;color:#fff;text-transform:uppercase;letter-spacing:.3px}
.footer ul{list-style:none;margin-top:22px}
.footer li{font-size:13px;line-height:30px;color:#fff}
.social{width:38px;height:38px;border:1px solid rgba(255,255,255,.35);border-radius:4px}
</style>
</head>
<body>

<header>
  <div class="abs topbar"></div>
  <div class="abs topbar-item" style="left:830px">
    <svg width="13" height="10" viewBox="0 0 13 10"><rect x=".5" y=".5" width="12" height="9" fill="none" stroke="#E23B3B"/><path d="M.5 .5l6 5 6-5" fill="none" stroke="#E23B3B"/></svg>info@tavonex4.com
  </div>
  <div class="abs topbar-item" style="left:1008px">
    <svg width="12" height="12" viewBox="0 0 24 24"><path d="M6.6 10.8a15 15 0 006.6 6.6l2.2-2.2c.3-.3.7-.4 1-.2 1.1.4 2.3.6 3.6.6.6 0 1 .4 1 1V20c0 .6-.4 1-1 1A17 17 0 013 4c0-.6.4-1 1-1h3.5c.6 0 1 .4 1 1 0 1.3.2 2.5.6 3.6.1.3 0 .7-.2 1z" fill="#E23B3B"/></svg>1800 555 0148
  </div>
  <div class="abs brand" style="left:86px;top:32px"><span class="brand-mark"></span>Tavonex4.com</div>
  <nav class="abs nav" style="left:0">
    <a class="active" style="left:586px">Home</a>
    <a style="left:675px">About</a>
    <a style="left:767px">Services</a>
    <a style="left:877px">Projects</a>
  </nav>
  <div class="abs btn" style="left:969px;top:63px;width:145px;height:47px;text-transform:none;letter-spacing:0;font-size:14px;font-weight:600">Contact</div>
  <div class="abs header-rule"></div>
</header>

<section>
  <div class="photo" role="img" aria-label="Columned federal government building with waving American flags" style="left:0;top:126px;width:1200px;height:572px;background:linear-gradient(180deg,#7E9AB8 0%,#5C6E80 35%,#4B5A62 70%,#4E6A3C 100%)"></div>
  <div class="abs" style="left:0;top:126px;width:1200px;height:572px;background:rgba(10,20,35,.25)"></div>
  <h1 class="abs hero-title">Architecture for Federal<br>Government Agencies<br>and Defense</h1>
  <div class="abs hero-btn">OUR PROJECTS →</div>
</section>

<section>
  <div class="abs eyebrow" style="left:86px;top:732px">About us</div>
  <h2 class="abs section-title" style="left:86px;top:748px;width:440px">We Design and Build Federal Government Agencies and Defense</h2>
  <p class="abs para" style="left:587px;top:753px;width:530px;font-size:13.5px">Lorem ipsum dolor sit amet, consectetur adipiscing elit. Quisque congue eros rhoncus nulla consequat, in rhoncus massa finibus. Cras tempus arcu leo, eu condimentum diam sollicitudin vel.</p>
  <div class="abs btn" style="left:587px;top:853px;width:185px;height:52px">Read more →</div>
</section>

<div class="photo" role="img" aria-label="Hands drafting an architectural floor plan with a pencil beside a calculator" style="left:0;top:948px;width:1114px;height:367px;background:linear-gradient(120deg,#6E6A64 0%,#A8A294 40%,#C9BFA8 60%,#8D8A84 100%)"></div>

<section>
  <div class="abs" style="left:84px;top:1315px;width:1116px;height:438px;background:var(--blue-5)"></div>
  <div class="abs eyebrow" style="left:107px;top:1353px">Project</div>
  <h2 class="abs section-title" style="left:107px;top:1369px">Best Project That<br>We’ve Completed</h2>
  <svg class="abs" style="left:1075px;top:1402px" width="36" height="22" viewBox="0 0 36 22"><path d="M0 11h33M24 2l9 9-9 9" fill="none" stroke="var(--blue)" stroke-width="2.5"/></svg>

  <article class="abs proj-card" style="left:107px;top:1472px">
    <div class="img" role="img" aria-label="White neoclassical government building with dome under blue sky" style="background:linear-gradient(180deg,#3E7FD0 0%,#9CC0E8 40%,#D9DDE0 65%,#6E8A4E 100%)"></div>
    <h3>Halvern Regional Works Office, Merrow District, SDVOSB Multiple Award Task</h3>
    <p>Aliquam consequat mi non ex viverra placerat. Duis uleu leo nec accumsan.</p>
    <div class="btn">Read more →</div>
  </article>
  <article class="abs proj-card" style="left:451px;top:1472px">
    <div class="img" role="img" aria-label="Modern white federal office building with colonnade" style="background:linear-gradient(180deg,#2B63C4 0%,#7FA9E4 35%,#DADDE2 60%,#8E9096 100%)"></div>
    <h3>Halvern Regional Works Office, Merrow District, SDVOSB Multiple Award Task</h3>
    <p>Aliquam consequat mi non ex viverra placerat. Duis uleu leo nec accumsan.</p>
    <div class="btn">Read more →</div>
  </article>
  <article class="abs proj-card" style="left:794px;top:1472px">
    <div class="img" role="img" aria-label="Classical stone building with columns and square in front" style="background:linear-gradient(180deg,#8FB3DD 0%,#CBBEA2 45%,#A58F6C 75%,#6D5F4E 100%)"></div>
    <h3>Halvern Regional Works Office, Merrow District, SDVOSB Multiple Award Task</h3>
    <p>Aliquam consequat mi non ex viverra placerat. Duis uleu leo nec accumsan.</p>
    <div class="btn">Read more →</div>
  </article>
</section>

<section>
  <div class="photo" role="img" aria-label="Technical drawings with compass, pen and eyeglasses" style="left:572px;top:2027px;width:485px;height:554px;background:linear-gradient(135deg,#C6CACE 0%,#E6E8EA 50%,#B9BEC4 100%)"></div>
  <div class="abs" style="left:143px;top:2082px;width:485px;height:440px;background:var(--blue-5)"></div>
  <div class="abs eyebrow" style="left:187px;top:2131px">Why choose us</div>
  <h2 class="abs section-title" style="left:187px;top:2145px">Let's start your<br>next project today</h2>
  <p class="abs para" style="left:187px;top:2246px;width:405px">Integer sit amet ex ac nuncrices maximus in ut orci. Sed commodo condimtum nisl, in dignissim ante bibendum ac. Fusce eget turpis sit amilisis rhoncus. Pellentesque nec dui ultrices. Sed posuere quam in augue faucibus, nec elementum dolor posuere.</p>
  <div class="abs" style="left:180px;top:2382px;width:112px;height:112px;border-radius:50%;border:6px solid var(--blue);background:#fff"></div>
</section>

<section>
  <div class="photo" role="img" aria-label="Government building facade with American flag at dusk" style="left:0;top:2632px;width:1200px;height:391px;background:linear-gradient(180deg,#2E3A4C 0%,#3D4656 60%,#2A3444 100%)"></div>
  <div class="abs" style="left:0;top:3023px;width:1200px;height:483px;background:var(--blue-5)"></div>
  <div class="abs eyebrow" style="left:84px;top:2728px;color:#fff">Our services</div>
  <h2 class="abs section-title" style="left:84px;top:2745px;color:#fff">We Provide Quality Services</h2>

  <article class="abs svc-card" style="left:84px;top:2832px">
    <div class="icon"><svg width="70" height="70" viewBox="0 0 70 70"><circle cx="48" cy="22" r="20" fill="var(--blue-4)"/><rect x="10" y="20" width="44" height="36" fill="none" stroke="var(--blue)" stroke-width="2.5"/><path d="M18 48V30h12v18M30 38h16" fill="none" stroke="var(--blue)" stroke-width="2.5"/></svg></div>
    <h3>Architecture Design</h3>
    <p>Fusce eget tus sit amilisis rhoncus. Pellentesque nec dui ultrices. Sed posuere quam</p>
    <div class="btn">Read more →</div>
  </article>
  <article class="abs svc-card" style="left:438px;top:2832px">
    <div class="icon"><svg width="70" height="70" viewBox="0 0 70 70"><circle cx="48" cy="22" r="20" fill="var(--blue-4)"/><circle cx="34" cy="38" r="20" fill="none" stroke="var(--blue)" stroke-width="2.5" stroke-dasharray="6 4"/><circle cx="34" cy="38" r="12" fill="none" stroke="var(--blue)" stroke-width="2.5"/><path d="M28 42v-6l6-4 6 4v6z" fill="none" stroke="var(--blue)" stroke-width="2"/></svg></div>
    <h3>Engineer</h3>
    <p>Fusce eget tus sit amilisis rhoncus. Pellentesque nec dui ultrices. Sed posuere quam</p>
    <div class="btn">Read more →</div>
  </article>
  <article class="abs svc-card" style="left:792px;top:2832px">
    <div class="icon"><svg width="70" height="70" viewBox="0 0 70 70"><circle cx="48" cy="22" r="20" fill="var(--blue-4)"/><path d="M24 24a11 11 0 0122 0z" fill="none" stroke="var(--blue)" stroke-width="2.5"/><path d="M14 30h42M16 58h38M20 34v20M28 34v20M36 34v20M44 34v20M50 34v20" stroke="var(--blue)" stroke-width="2.5"/></svg></div>
    <h3>Design Build</h3>
    <p>Fusce eget tus sit amilisis rhoncus. Pellentesque nec dui ultrices. Sed posuere quam</p>
    <div class="btn">Read more →</div>
  </article>

  <div class="abs logo-strip">
    <div class="logo-cell"><span class="logo-shape"></span><span class="logo-bar"></span></div>
    <div class="logo-cell"><span class="logo-shape" style="border-radius:4px"></span><span class="logo-bar"></span></div>
    <div class="logo-cell"><span class="logo-shape"></span><span class="logo-bar"></span></div>
    <div class="logo-cell"><span class="logo-shape" style="border-radius:4px"></span><span class="logo-bar"></span></div>
  </div>
</section>

<section>
  <div class="photo" role="img" aria-label="Faint dotted world map background" style="left:40px;top:3560px;width:1120px;height:560px;background:radial-gradient(ellipse at center,#EEF1F4 0%,#F7F8FA 55%,#fff 80%)"></div>
  <div class="abs eyebrow" style="left:84px;top:3633px">Testimonials</div>
  <h2 class="abs section-title" style="left:84px;top:3649px">What People Say About Us</h2>

  <article class="abs review" style="left:84px;top:3721px">
    <div class="avatar">R</div><h3>Rolf Dannecker</h3><div class="role">CEO</div><div class="stars">★★★★★</div>
    <p>"Aliquam condimentum urna vel velit sodales, in sollicitudin ex lacinia. Suspendisse sit amet mi ultricies, ultrices libero nec, vehicula augue."</p>
    <div class="src"></div>
  </article>
  <article class="abs review" style="left:434px;top:3721px">
    <div class="avatar">R</div><h3>Rolf Dannecker</h3><div class="role">CEO</div><div class="stars">★★★★★</div>
    <p>"Aliquam condimentum urna vel velit sodales, in sollicitudin ex lacinia. Suspendisse sit amet mi ultricies, ultrices libero nec, vehicula augue."</p>
    <div class="src"></div>
  </article>
  <article class="abs review" style="left:784px;top:3721px">
    <div class="avatar">R</div><h3>Rolf Dannecker</h3><div class="role">CEO</div><div class="stars">★★★★★</div>
    <p>"Aliquam condimentum urna vel velit sodales, in sollicitudin ex lacinia. Suspendisse sit amet mi ultricies, ultrices libero nec, vehicula augue."</p>
    <div class="src"></div>
  </article>
</section>

<footer class="abs footer">
  <div class="abs" style="right:86px;top:42px;color:#fff;font:700 11px/1 Inter,sans-serif;letter-spacing:1.4px">↑ GO TO TOP</div>
  <div class="abs" style="left:84px;top:76px;width:1030px;height:1px;background:rgba(255,255,255,.2)"></div>

  <div class="abs brand" style="left:86px;top:170px;color:#fff"><span class="brand-mark" style="background:var(--blue-2)"></span>Tavonex4.com</div>
  <div class="abs social" style="left:138px;top:272px"></div>
  <div class="abs social" style="left:186px;top:272px"></div>
  <div class="abs social" style="left:234px;top:272px"></div>

  <div class="abs" style="left:430px;top:152px">
    <h4>Contact info</h4>
    <ul><li>12 Corvel Lane, Brantwood,</li><li style="margin-top:-4px">Australia</li><li>info@tavonex4.com</li><li>1800 555 0148</li></ul>
  </div>
  <div class="abs" style="left:746px;top:152px">
    <h4>Quick links</h4>
    <ul><li>Home</li><li>About</li><li>Services</li><li>Projects</li><li>Contact</li></ul>
  </div>
  <div class="abs" style="left:979px;top:152px">
    <h4>Services</h4>
    <ul><li>Architecture Design</li><li>Engineer</li><li>Design Build</li></ul>
  </div>

  <div class="abs" style="left:84px;top:416px;font-size:12px;color:#fff">© 2024 <span style="color:var(--blue-2)">Tavonex4</span>. All right reserved</div>
  <div class="abs" style="right:86px;top:416px;font-size:12px;color:#7F8FA6">June 18, 2024. Layout_4</div>
</footer>

</body>
</html>
```